Hair Restoration Center needs a new classy clean professional look for a new website.

We want a new look for our outdated website. We are a high end hair restoration company who deals with all kinds of hair loss for both men and women. We offer solutions to hair loss prevention or our state of the art non surgical hair restoration. Our look would be similar to the medical enhancement designs. We are doctor endorsed and very professional. We are looking for a clean look, positive vibe, strong imagery.
People with hair loss are often in distress, feeling a lack of self esteem, and looking for a reliable solution. the difference between our clients is some come to us for hair loss prevention or for hair restoration depends on how advanced their loss has become or the kind of loss. Younger people tend to be prevention candidates, often having treatments done at home, whereas medical loss for women or mens advanced hair loss become restoration clients. Prevention age ranges from early 20's to 40's and restoration can be any age if medical or for women and men usually late 30's onward.
Our site is dated and doesnt represent us well but if you want to read more about us you can visit www.velmarhair.com. the photos attached here are also blown up in large posters throughout the office and models of non surgical restoration. For a large selection of photos please go to the link. There is one before photo but many types of after photos for each model.
There are more colours of the logos available in grey and dark greyish green available. http://www.velmarhair.com/download/Models_Before_After.zip
Our primary means of new business comes from internet searches.
Your task is to design the home page design but the site will need to link into a women's section and a mens section along with gender neutral educational pages. You will get a feel from our current site. Www.velmarhair.com
Content will be rewritten but I gave a couple samples to use as fill in. Our current site has way to much content and I would like to step away from all of it. you can utilize fill in text of any kind as a sample
To get a feel of our office, it is black granite, white rock features with floor to ceiling beautiful city and ocean views. very high end.

Target Market(s)

men and women of all ages as listed above

Industry/Entity Type

Internet

Number of Pages Required

1 page

Requirements
Must have
• imagery and design that creates emotion - consider that people with hair loss is emotional buyers and the sites image needs to speak to that.
• it would create a sense of security and confidence in choosing us to help them in a time of need.
• also a sense of ease flowing through the site where women can go to a dedicated area and men have their own area of the site. each area needs to cater to the two divisions prevention and restoration and also speak and visually appeal to the different sexes. You can get a feel of this by visiting www.velmarhair.com
Nice to have
• I have video footage from a green room that could be worked on to add in
• wordpress preferred
Should not have
• no humour
• do not focus on the before photos as primary focus but the afters with the ability to see the before.

```html
<!DOCTYPE html>
<html lang="en">
<head>
<meta charset="utf-8">
<title>Velmar Hair Restoration</title>
<link href="https://fonts.googleapis.com/css2?family=Raleway:wght@300;400;500&family=Open+Sans:ital,wght@0,400;0,600;1,400&display=swap" rel="stylesheet">
<style>
:root{
  --ink:#2b3435;
  --slate:#4d5e60;
  --nav-top:#5b6c6d;
  --nav-bottom:#2f3d3f;
  --light:#e1e1e1;
  --muted:#777;
  --white:#fff;
  --footer:#1f2829;
}
*{margin:0;padding:0;box-sizing:border-box}
html,body{width:742px;height:1200px;overflow:hidden;background:var(--white)}
body{position:relative;font-family:"Open Sans",sans-serif;color:var(--ink)}
.abs{position:absolute}
h1,h2,h3{font-weight:400}

/* header */
.brand{left:122px;top:12px;font-family:"Raleway",sans-serif;font-weight:400;font-size:30px;color:var(--slate);letter-spacing:.5px;display:flex;align-items:center;gap:8px}
.brand-dot{width:12px;height:12px;border-radius:50%;background:var(--slate)}
.call{right:118px;top:28px;text-align:right;font-family:"Raleway",sans-serif}
.call small{display:block;font-size:7px;color:var(--muted);letter-spacing:.3px}
.call strong{font-weight:400;font-size:12px;color:var(--ink);display:flex;align-items:center;gap:2px;justify-content:flex-end}

.nav{left:0;top:62px;width:742px;height:31px;background:linear-gradient(var(--nav-top),var(--nav-bottom))}
.nav ul{list-style:none;position:absolute;left:118px;top:0;display:flex;height:31px}
.nav li{font-family:"Raleway",sans-serif;font-size:7.4px;color:var(--white);line-height:31px;padding:0 12.5px;font-weight:500}
.nav li.active{background:#1c2526;padding:0 11px}

/* hero */
.hero-band{left:0;top:93px;width:742px;height:289px;background:linear-gradient(90deg,#d4d4d4,#e2e2e2 50%,#d6d6d6)}
.hero-photo{left:365px;top:93px;width:280px;height:289px;background:radial-gradient(ellipse at 50% 35%,#6a3e2c 0%,#4e2a1d 45%,rgba(78,42,29,0) 72%),linear-gradient(#cfcfcf,#cfcfcf)}
.hero-title{left:118px;top:182px;font-family:"Raleway",sans-serif;font-weight:400;font-size:18px;line-height:22px;color:#222;white-space:nowrap}
.hero-sub{left:118px;top:207px;font-family:"Raleway",sans-serif;font-size:14.5px;line-height:18px;font-weight:400;color:#222;white-space:nowrap}
.hero-copy{left:118px;top:233px;width:240px;font-size:6.3px;line-height:10.5px;color:var(--muted)}
.btn{left:118px;top:262px;width:65px;height:19px;background:linear-gradient(#5b6c6d,#34433f);border-radius:2px;color:var(--white);font-size:6.5px;text-align:center;line-height:19px;font-weight:600}
.arrow{width:34px;height:34px;border-radius:50%;background:var(--white);top:206px;display:flex;align-items:center;justify-content:center}

/* intro */
.intro-title{left:0;top:418px;width:742px;text-align:center;font-family:"Raleway",sans-serif;font-size:14px;line-height:21px;color:#222}
.intro-copy{left:125px;top:468px;width:492px;text-align:center;font-size:5.6px;line-height:11px;color:#444}

.card{top:542px;width:164px;height:152px;border:1px solid #d6d6d6;background:var(--white);box-shadow:0 1px 2px rgba(0,0,0,.08)}
.card-img{height:84px}
.card h3{font-family:"Raleway",sans-serif;font-weight:400;font-size:11px;margin:9px 0 0 14px;color:#333}
.card p{font-size:5.7px;line-height:9.5px;color:var(--muted);margin:3px 14px 0}
.card a{display:block;font-size:6.3px;font-weight:600;color:#333;margin:4px 0 0 14px;text-decoration:none}

/* how it works */
.how-band{left:0;top:734px;width:742px;height:214px;background:linear-gradient(#4f6264,#1f2c2d)}
.how-title{left:119px;top:783px;font-family:"Raleway",sans-serif;font-weight:300;font-size:20px;line-height:24px;color:var(--white)}
.how-copy{left:121px;top:815px;width:232px;font-size:5.6px;line-height:9.6px;color:#d4dada}
.how-copy p+p{margin-top:5px}
.video{left:406px;top:776px;width:215px;height:130px;border:3px solid #5e6b6c;box-shadow:0 2px 6px rgba(0,0,0,.5);background:linear-gradient(90deg,#9a9a9a,#8c8c8c 40%,#a79aa8 60%,#8e8e8e)}
.play{left:500px;top:827px;width:27px;height:27px;border-radius:50%;background:var(--white);display:flex;align-items:center;justify-content:center}

/* testimonials */
.testi-band{left:0;top:948px;width:742px;height:186px;background:var(--light)}
.testi-title{left:0;top:972px;width:742px;text-align:center;font-family:"Raleway",sans-serif;font-weight:400;font-size:17px;line-height:20px;color:#333}
.quote{top:1008px;width:249px;height:95px;background:var(--white);border:1px solid #cfcfcf}
.avatar{left:11px;top:18px;width:49px;height:49px;border-radius:50%;border:2px solid #ddd;background:radial-gradient(circle,#a98466,#5d4030)}
.quote blockquote{position:absolute;left:68px;top:15px;width:170px;font-size:5.8px;line-height:11.2px;color:#666;font-style:italic}
.quote blockquote b{font-style:normal;font-size:12px;color:#aaa;font-family:Georgia,serif;line-height:5px;vertical-align:-3px;margin-right:3px}
.quote cite{position:absolute;left:68px;top:70px;font-size:6.2px;font-style:normal;color:#333}

/* footer */
.footer-band{left:0;top:1134px;width:742px;height:66px;background:var(--footer)}
.foot-links{left:119px;top:1155px;font-family:"Raleway",sans-serif;font-size:7.4px;color:var(--white)}
.copyright{left:119px;top:1171px;font-size:6px;color:#9aa3a3}
.social{left:564px;top:1155px;display:flex;gap:9px}
.social span{width:12px;height:12px;border-radius:50%;background:var(--white)}
</style>
</head>
<body>
<header>
  <div class="abs brand"><span class="brand-dot"></span>Velmar</div>
  <div class="abs call"><small>CALL US NOW</small>
    <strong><svg width="9" height="9" viewBox="0 0 24 24"><path fill="#2b3435" d="M6.6 10.8a15 15 0 0 0 6.6 6.6l2.2-2.2a1 1 0 0 1 1-.25 11.4 11.4 0 0 0 3.6.57 1 1 0 0 1 1 1V20a1 1 0 0 1-1 1A17 17 0 0 1 3 4a1 1 0 0 1 1-1h3.5a1 1 0 0 1 1 1c0 1.25.2 2.45.57 3.57a1 1 0 0 1-.25 1z"/></svg>1800 555 0142</strong></div>
</header>
<nav class="abs nav"><ul>
  <li class="active">HOME</li><li>MEN</li><li>WOMEN</li><li>NATURAL ADVANTAGE</li><li>BLOG</li><li>HAIRLOSS FACTS</li><li>TESTIMONIALS</li><li>CONTACT</li>
</ul></nav>

<section>
  <div class="abs hero-band"></div>
  <div class="abs hero-photo" role="img" aria-label="Portrait of a woman with full curly auburn hair in a plum top"></div>
  <h1 class="abs hero-title">Its not just hair replacement,</h1>
  <div class="abs hero-sub">its confidence replacement!</div>
  <p class="abs hero-copy">Mauris vel lacus vitae felis vestibulum volutpat Etiam est nunc venenatis in tristique eu imperdiet ac nisl Cum sociis natoque penatibus</p>
  <div class="abs btn">READ MORE</div>
  <div class="abs arrow" style="left:59px"><svg width="10" height="16" viewBox="0 0 10 16"><path d="M8 1L2 8l6 7" fill="none" stroke="#333" stroke-width="1.4"/></svg></div>
  <div class="abs arrow" style="left:647px"><svg width="10" height="16" viewBox="0 0 10 16"><path d="M2 1l6 7-6 7" fill="none" stroke="#333" stroke-width="1.4"/></svg></div>
</section>

<section>
  <h2 class="abs intro-title">Did you know that in North America alone,<br>50 million men and 30 million women suffer from hair loss ?</h2>
  <p class="abs intro-copy">Picture in your mind, the last time that you looked into the mirror and saw what you liked. To see the person you used to know; confident, secure, sexy with a great head of hair. Now imagine if you can have all this again, how much is this worth to you? Most of you would say priceless but don't know their options or afraid of the consequences of wearing to age old wigs and toupees. To see the leaps and bounds available today in non-surgical replacement could leave you speechless.<br>Todays advancements, available through only some of the finest hair replacement centres, have created what is called a derma-lense application.</p>

  <article class="abs card" style="left:118px">
    <div class="card-img" role="img" aria-label="Glass bottles of natural oils on a wooden tray" style="background:linear-gradient(#c9d4a8,#8aa05a 55%,#6b3d22)"></div>
    <h3>Natural Advantage</h3>
    <p>Mauris vel lacus vitae felis vestibulum volutpat Etiam est nunc venenatis in tristique</p>
    <a>Read More</a>
  </article>
  <article class="abs card" style="left:289px">
    <div class="card-img" role="img" aria-label="Young woman with sleek brown hair" style="background:linear-gradient(90deg,#b5b5b5,#6b4030 45%,#5a3424 60%,#b0b0b0)"></div>
    <h3>Why Hairloss</h3>
    <p>Mauris vel lacus vitae felis vestibulum volutpat Etiam est nunc venenatis in tristique</p>
    <a>Read More</a>
  </article>
  <article class="abs card" style="left:461px">
    <div class="card-img" role="img" aria-label="A smiling man and woman side by side" style="background:linear-gradient(90deg,#3a3a3a,#6a5a50 50%,#5a3a2a 55%,#c8c8c8)"></div>
    <h3>Men &amp; Women</h3>
    <p>Mauris vel lacus vitae felis vestibulum volutpat Etiam est nunc venenatis in tristique</p>
    <a>Read More</a>
  </article>
</section>

<section>
  <div class="abs how-band"></div>
  <h2 class="abs how-title">How it Works</h2>
  <div class="abs how-copy">
    <p>Here at Velmar's, we focus much time and effort helping women find an optimal personalized hair loss solution that is best suited to their individual needs. Women's hair loss is treatable and effective solutions are better than ever.</p>
    <p>Be it hair restoration or hair loss prevention, we are driven and highly committed to bringing you satisfaction using state of the art techniques from any one of our wide variety of services detailed in this website.</p>
  </div>
  <div class="abs video" role="img" aria-label="Video still of a man with styled hair in a pink vest"></div>
  <div class="abs play"><svg width="10" height="12" viewBox="0 0 10 12"><path d="M1 0l9 6-9 6z" fill="#111"/></svg></div>
</section>

<section>
  <div class="abs testi-band"></div>
  <h2 class="abs testi-title">Testimonials</h2>
  <div class="abs quote" style="left:118px">
    <div class="abs avatar" role="img" aria-label="Client portrait, woman with blonde hair"></div>
    <blockquote><b>&ldquo;</b>Mauris vel lacus vitae felis vestibulum volutpat Etiam est nunc venenatis in tristique eu imperdiet ac nisl Cum sociis natoque penatibus et magnis dis parturient montes nascetur ridiculus mus In iaculis facilisis</blockquote>
    <cite>By Author Name, City Location</cite>
  </div>
  <div class="abs quote" style="left:374px">
    <div class="abs avatar" role="img" aria-label="Client portrait, woman with dark curly hair"></div>
    <blockquote><b>&ldquo;</b>Lcus vitae felis vestibulum volutpat Etiam est nunc venenatis in tristique eu imperdiet ac nisl Cum sociis natoque penatibus et magnis dis parturient montes nascetur ridiculus mus In iaculi</blockquote>
    <cite>By Author Name, City Location</cite>
  </div>
</section>

<footer>
  <div class="abs footer-band"></div>
  <div class="abs foot-links">HOME &nbsp;|&nbsp; MEN &nbsp;|&nbsp; WOMEN &nbsp;|&nbsp; NATURAL ADVANTAGE &nbsp;|&nbsp; BLOG &nbsp;|&nbsp; HAIRLOSS FACTS &nbsp;|&nbsp; TESTIMONIALS &nbsp;|&nbsp; CONTACT</div>
  <div class="abs copyright">© 2015 Company Name &nbsp;All right reserved &nbsp;Term of Use</div>
  <div class="abs social"><span></span><span></span><span></span></div>
</footer>
</body>
</html>
```